Dale Finch - Acoustic Album Cover

I am a musical artist releasing my first full-length solo album. It is composed of nine original "percussive" acoustic fingerstyle songs. Some of my earlier recordings (not for this album) are available at http://www.tunecradle.example/dalefinch for reference. I am looking for creative album art and need both a front cover and back cover/track listing for physical CD replication and online album art purposes. I am open to a more "natural" design using the pictures included in the uploaded files section or to a more artistic design that doesn't use any of the included pictures at all. The name of the album is "Lanterns", and artist is "Dale Finch" (me). The track list is:

01) Meadow Shuffle
02) Pinwheel
03) Echoes of Marlow
04) Nested Up
05) Walk Along
06) The Quiet Ridge
07) Unfolding
08) Dusk on Pellman Avenue
09) Lorena's Tune

Here are some album art examples from professional acoustic artists in the same style as a reference:

https://img.vidplume.example/v/QxRtz81LmWa/cover.jpg
http://stringloft.example/uploads/2009/12/Low-Bridge-cover-small.jpg
https://plumfox.cdnhost.example/ImageGen.ashx?image=/media/20417/Len-Vobeck.jpg&width=500
https://files.openpedia.example/commons/4/27/Tobias_Kernwald-Driftwood_album.jpg
https://media.soundmoth.example/imageserver/images/Alb.918273645/500x500.jpg
https://img.shopwharf.example/images/I/73KpqB2WzuT._SY355_.jpg
https://img.shopwharf.example/images/I/29GhvN5XroM._SY355_.jpg

As you can see, there is a broad mix of both art-based and photograph-based album covers for artists of this style. I am open to either approach, and an example of each would be preferred if time permits.

Thank you for considering my project and for sharing your artistic talents!

-Dale

Target Market(s)

Music app listeners (Tunevault, Melodrift, Cadenzo) on any app which displays the album art as part of the artist information pane.

Industry/Entity Type

Music Download

Font styles to use
Serif
Sans Serif
Decorative

Colors

Designer to choose colors to be used in the design.

Requirements
Must have
• The project must have the album name and artist name on the front cover artwork, as well as the track listing on the back cover artwork.
Nice to have
• Some original, creative album artwork would be nice to have, but I would settle on well-done picture-based album designs (photos included) as well.
Should not have
• The project should not have too "stuffy" of a feel (similar to a lot of classical guitar album artwork which usually features the artist in a turtleneck smiling at the camera with guitar in lap).

```html
<!DOCTYPE html>
<html lang="en">
<head>
<meta charset="utf-8">
<title>Dale Finch – Lanterns – Back Cover</title>
<link rel="stylesheet" href="https://fonts.googleapis.com/css2?family=Open+Sans:wght@400&display=swap">
<style>
  :root {
    --paper: #ffffff;
    --brick-light: #6b4536;
    --brick-mid: #55372c;
    --brick-dark: #3b2822;
    --type: #ffffff;
  }
  html, body {
    margin: 0;
    padding: 0;
    overflow: hidden;
    background: var(--paper);
  }
  .cover {
    position: relative;
    width: 1200px;
    height: 1200px;
    background: var(--paper);
    overflow: hidden;
    font-family: "Open Sans", sans-serif;
    color: var(--type);
  }
  .photo-band {
    position: absolute;
    left: 0;
    width: 1200px;
    background: linear-gradient(135deg, var(--brick-light) 0%, var(--brick-mid) 45%, var(--brick-dark) 100%);
  }
  .photo-band--main { top: 175px; height: 709px; }
  .photo-band--lower { top: 898px; height: 126px; }
  .tracklist {
    position: absolute;
    left: 98px;
    top: 257px;
    margin: 0;
    padding: 0;
    list-style: none;
    font-size: 30px;
    line-height: 60px;
    letter-spacing: 0.3em;
    white-space: nowrap;
  }
  .tracklist .num { margin-right: 0.2em; }
  .artist-name,
  .album-title {
    position: absolute;
    right: 40px;
    margin: 0;
    font-weight: 400;
    font-size: 60px;
    line-height: 1;
    letter-spacing: 0.25em;
    margin-right: -0.25em;
    white-space: nowrap;
  }
  .artist-name { top: 801px; }
  .album-title { top: 930px; }
</style>
</head>
<body>
  <main class="cover">
    <div class="photo-band photo-band--main" role="img" aria-label="Photo of the guitarist playing an acoustic guitar against a red brick wall, darkened"></div>
    <div class="photo-band photo-band--lower" role="img" aria-label="Continuation of the brick wall photo below the dividing stripe"></div>

    <ol class="tracklist">
      <li><span class="num">01)</span> Meadow Shuffle</li>
      <li><span class="num">02)</span> Pinwheel</li>
      <li><span class="num">03)</span> Echoes of Marlow</li>
      <li><span class="num">04)</span> Nested Up</li>
      <li><span class="num">05)</span> Walk Along</li>
      <li><span class="num">06)</span> The Quiet Ridge</li>
      <li><span class="num">07)</span> Unfolding</li>
      <li><span class="num">08)</span> Dusk on Pellman Avenue</li>
      <li><span class="num">09)</span> Lorena's Tune</li>
    </ol>

    <h1 class="artist-name">DALE FINCH</h1>
    <h2 class="album-title">LANTERNS</h2>
  </main>
</body>
</html>
```